business card design

i would like business cards designed. My business provides trade qualified personnel to the mining industry to work on heavy mobile equipment.
please put a excavator(digger) in the background in one design and have one design without so i can compare the difference.
also add info:
my logo(attached) and "mobile equipment repair and maintenance"
name: Gavin Stroud
address: 42 Brindle RD Marlow Heights WA.
mobile: 0461902738
email: gavin@hollowvex.com

```html
<!DOCTYPE html>
<html lang="en">
<head>
<meta charset="utf-8">
<title>Hollowvex Maintenance Services – Business Card</title>
<link href="https://fonts.googleapis.com/css2?family=Montserrat:wght@400;600;800&display=swap" rel="stylesheet">
<style>
  :root {
    --backdrop: #2b2b2d;
    --card: #141415;
    --accent: #4a78c8;
    --ink: #f2f2f2;
    --ink-muted: #d8d8d8;
    --ink-soft: #bdbdbd;
  }
  * { box-sizing: border-box; margin: 0; padding: 0; }
  html, body {
    width: 1200px; height: 900px; overflow: hidden;
    background: var(--backdrop);
    font-family: "Montserrat", Arial, sans-serif;
  }
  .sheet {
    width: 1200px; height: 900px;
    display: flex; flex-direction: column; align-items: center; justify-content: center;
    gap: 40px;
  }
  .card {
    position: relative;
    width: 700px; height: 400px;
    background: var(--card);
    border-bottom: 8px solid var(--accent);
    box-shadow: 0 12px 30px rgba(0,0,0,.45);
    overflow: hidden;
  }
  .brand-name {
    font-weight: 800; color: var(--ink);
    letter-spacing: 1px; line-height: 1; white-space: nowrap;
  }
  .brand-sub {
    font-weight: 600; color: var(--accent);
    letter-spacing: 1.5px; text-transform: uppercase; white-space: nowrap;
  }
  /* front */
  .card-front .brand {
    position: absolute; left: 50px; top: 140px; width: 310px;
  }
  .card-front .brand-name { font-size: 38px; }
  .card-front .brand-sub { font-size: 10.5px; margin-top: 10px; }
  .divider {
    position: absolute; left: 390px; top: 110px;
    width: 1.5px; height: 170px; background: var(--accent);
  }
  .contact {
    position: absolute; left: 420px; top: 115px;
    color: var(--ink-muted); font-size: 17px; line-height: 1.5;
  }
  .contact-name {
    color: var(--accent); font-weight: 800; font-size: 22px;
    letter-spacing: 1px; text-transform: uppercase; margin-bottom: 8px;
  }
  .contact-line { display: flex; align-items: center; gap: 8px; }
  .contact-line svg { width: 14px; height: 14px; flex: none; }
  /* back */
  .card-back { display: flex; flex-direction: column; align-items: center; justify-content: center; }
  .card-back .brand-name { font-size: 64px; color: var(--ink-soft); }
  .card-back .brand-sub { font-size: 14px; margin-top: 12px; color: #9a9a9a; }
  .tagline {
    margin-top: 46px; color: var(--ink);
    font-size: 17px; letter-spacing: 1.5px; text-transform: uppercase;
  }
</style>
</head>
<body>
<main class="sheet">
  <section class="card card-front">
    <div class="brand">
      <div class="brand-name">HOLLOWVEX</div>
      <div class="brand-sub">Maintenance Services Pty Ltd</div>
    </div>
    <div class="divider"></div>
    <div class="contact">
      <div class="contact-name">Gavin Stroud</div>
      <div>42 Brindle RD</div>
      <div>Marlow Heights WA.</div>
      <div class="contact-line">
        <svg viewBox="0 0 16 16" aria-hidden="true"><path d="M4 1.5l2.5 3-1.5 1.8c.8 1.8 2.2 3.2 4 4l1.8-1.5 3 2.5-1.3 2.4C7.5 13.5 2.5 8.5 1.6 2.8z" fill="var(--accent)"/></svg>
        0461902738
      </div>
      <div class="contact-line">
        <svg viewBox="0 0 16 16" aria-hidden="true"><rect x="1" y="3" width="14" height="10" fill="var(--accent)"/><path d="M1 3l7 6 7-6" fill="none" stroke="var(--card)" stroke-width="1.4"/></svg>
        gavin@hollowvex.com
      </div>
    </div>
  </section>

  <section class="card card-back">
    <div class="brand-name">HOLLOWVEX</div>
    <div class="brand-sub">Maintenance Services Pty Ltd</div>
    <div class="tagline">Mobile Equipment Repair and Maintenance</div>
  </section>
</main>
</body>
</html>
```